Business Card Design

We just need these details on one side of card and logo on the other.

Industry/Entity Type

Business

Contact Information for Business Card

Colette Marsh | Artist
87 Tillbrook Lane
Dunmore Heights Vic 3172
# 0418 207 913 | 03 9386 2417
colette@colettemarsh-example.com
colettesstudio-example.com.au

```html
<!DOCTYPE html>
<html lang="en">
<head>
<meta charset="utf-8">
<title>Colette's Studio – Business Card</title>
<link rel="stylesheet" href="https://fonts.googleapis.com/css2?family=Marcellus&family=Questrial&display=swap">
<style>
  :root {
    --canvas-bg: #e9e7e4;
    --card-black: #0d0d0d;
    --card-white: #fafafa;
    --logo-ink: #f2f2f2;
    --text-grey: #6a6a6a;
    --name-grey: #4a4a4a;
    --mark-dark: #2a2a2a;
    --mark-light: #dcdcdc;
  }
  * { margin: 0; padding: 0; box-sizing: border-box; }
  html, body {
    width: 1200px;
    height: 900px;
    overflow: hidden;
    background: var(--canvas-bg);
  }
  .canvas {
    width: 1200px;
    height: 900px;
    display: flex;
    flex-direction: column;
    align-items: center;
    justify-content: center;
    gap: 44px;
  }
  .card {
    position: relative;
    width: 660px;
    height: 377px;
    overflow: hidden;
    box-shadow: 0 6px 18px rgba(0,0,0,0.14);
  }
  .card-front { background: var(--card-black); }
  .card-back { background: var(--card-white); }

  .faint-mark {
    position: absolute;
    border-radius: 50%;
  }
  .card-front .faint-mark {
    left: 300px; top: 120px; width: 230px; height: 170px;
    background: radial-gradient(closest-side, var(--mark-dark), rgba(42,42,42,0));
  }
  .card-back .faint-mark {
    left: 150px; top: 150px; width: 250px; height: 190px;
    background: radial-gradient(closest-side, var(--mark-light), rgba(220,220,220,0));
  }

  .brand-name {
    position: absolute;
    left: 0; right: 0; top: 150px;
    text-align: center;
    font-family: "Questrial", sans-serif;
    font-size: 52px;
    font-weight: 400;
    color: var(--logo-ink);
    letter-spacing: 1px;
  }

  .contact-name {
    position: absolute;
    left: 0; right: 0; top: 88px;
    text-align: center;
    font-family: "Marcellus", serif;
    font-size: 25px;
    letter-spacing: 3px;
    color: var(--name-grey);
    text-transform: uppercase;
  }
  .contact-details {
    position: absolute;
    left: 64px; top: 138px;
    list-style: none;
    font-family: "Questrial", sans-serif;
    font-size: 19px;
    line-height: 30px;
    color: var(--text-grey);
  }
</style>
</head>
<body>
  <main class="canvas">
    <section class="card card-front" aria-label="Card front">
      <div class="faint-mark" role="img" aria-label="Faint bird emblem decoration"></div>
      <p class="brand-name">Colette's Studio</p>
    </section>

    <section class="card card-back" aria-label="Card back">
      <div class="faint-mark" role="img" aria-label="Faint bird emblem decoration"></div>
      <h1 class="contact-name">Colette Marsh</h1>
      <ul class="contact-details">
        <li class="contact-address">Artist 87 Tillbrook Lane Dunmore Heights Vic 3172</li>
        <li class="contact-mobile">0418 207 913</li>
        <li class="contact-phone">03 9386 2417</li>
        <li class="contact-email">colette@colettemarsh-example.com</li>
        <li class="contact-web">colettesstudio-example.com.au</li>
      </ul>
    </section>
  </main>
</body>
</html>
```